Pitch book for Birchmere Property Partners.

Birchmere Partners is a new real estate investment company focused on multifamily (apartment) investments along the San Francisco Peninsula (in other parts of the world it is also referred to as flats). We need a professional Pitch Book i.e. brochure (digital and print) to raise equity from private investors. Read about “pitch book” on Lexipedia. The profile of the investor is conservative and must qualify as an accredited investor. Think high net worth individuals, CEOs and wealthy retiring couples. The investor that is attracted to real estate invest because it is low risk, produce cash flow and provide solid returns over the long term.

The brochure should convey trust, be highly professional and be clean and crisp. I attach a PowerPoint doc to be used as a copy for the brochure. I also attach a brochure of Halvert Crane – I like the look and feel, think it was designed with InDesign.

We will use the brochure at one-on-one meetings with investors where we will present on a laptop; we also need it in a format so that we can email it, print it and use it to be uploaded as a website.

I prefer the up and down scroll format (like you would do on a Mac) compared to PowerPoint but I am open to suggestions.

The photos I used in the PowerPoint presentation was found on the web, please use your own stock images.

Target Market(s)

High net worth individuals

Industry/Entity Type

Real Estate

Font styles to use
Serif

Requirements
Must have
• See attached Power Point
Nice to have
• See attached HVC brochure, I like the look and feel.
Should not have
• I am open to your ideas.

```html
<!DOCTYPE html>
<html lang="en">
<head>
<meta charset="utf-8">
<title>Birchmere Property Partners — Pitch Book</title>
<link rel="stylesheet" href="https://fonts.googleapis.com/css2?family=Tinos:wght@400;700&display=swap">
<style>
  :root {
    --backdrop: #d4d4d4;
    --paper: #ffffff;
    --teal: #5a8c80;
    --teal-dark: #4f8a7f;
    --teal-side: #8dbcb0;
    --teal-top: #b9ddd2;
    --heading-teal: #4d8376;
    --ink: #2b2b2b;
    --arrow-sand: #d8c8ae;
    --sky-top: #1d4f9c;
    --sky-mid: #5a6fb4;
    --horizon: #c98a7a;
    --water: #2c3f66;
    --shore: #3a2a22;
    --logo-ink: #111111;
  }
  * { margin: 0; padding: 0; box-sizing: border-box; }
  html, body { width: 1200px; height: 900px; overflow: hidden; }
  body {
    background: var(--backdrop);
    font-family: "Tinos", "Times New Roman", serif;
    position: relative;
  }
  .page {
    position: absolute;
    width: 660px;
    height: 520px;
    background: var(--paper);
    box-shadow: 0 4px 14px rgba(0,0,0,0.25);
    overflow: hidden;
  }
  /* Cover */
  .cover { left: 30px; top: 28px; z-index: 2; }
  .cover-photo {
    position: absolute; inset: 0;
    background:
      linear-gradient(180deg,
        var(--sky-top) 0%,
        var(--sky-mid) 30%,
        var(--horizon) 46%,
        #6b5a78 52%,
        var(--water) 60%,
        #23335a 75%,
        var(--shore) 100%);
  }
  .cover-band {
    position: absolute;
    left: 12px; right: 0; top: 390px;
    height: 98px;
    display: flex;
  }
  .cover-title {
    flex: 1;
    background: var(--teal);
    color: #fff;
    text-align: right;
    padding: 26px 28px 0 0;
  }
  .cover-title h1 {
    font-weight: 400;
    font-size: 27px;
    letter-spacing: 0.3px;
    line-height: 1;
  }
  .cover-title p {
    font-size: 17px;
    margin-top: 8px;
  }
  .brand-box {
    width: 155px;
    background: var(--paper);
    display: flex;
    flex-direction: column;
    align-items: center;
    justify-content: center;
    gap: 8px;
  }
  .brand-mark {
    width: 22px; height: 22px;
    background: var(--logo-ink);
  }
  .brand-name {
    font-size: 14px;
    color: var(--logo-ink);
    letter-spacing: 0.5px;
  }
  /* Lifecycle page */
  .lifecycle { left: 510px; top: 352px; z-index: 1; }
  .growth-chart {
    position: absolute; left: 0; top: 0;
  }
  .lifecycle-text {
    position: absolute;
    left: 395px; top: 62px;
  }
  .lifecycle-text h2 {
    font-weight: 400;
    font-size: 27px;
    line-height: 1.2;
    letter-spacing: 4px;
    color: var(--heading-teal);
  }
  .steps {
    list-style: none;
    margin-top: 28px;
  }
  .steps li {
    display: flex;
    align-items: center;
    gap: 18px;
    font-size: 15px;
    letter-spacing: 1px;
    color: var(--ink);
    height: 36.5px;
  }
  .steps svg { flex: none; }
</style>
</head>
<body>

<section class="page cover">
  <div class="cover-photo" role="img" aria-label="Photograph of a suspension bridge over the bay at dusk with city lights on the far shore"></div>
  <div class="cover-band">
    <div class="cover-title">
      <h1>SAN FRANCISCO PENINSULA</h1>
      <p>Multifamily Real Estate Investment</p>
    </div>
    <div class="brand-box">
      <span class="brand-mark"></span>
      <span class="brand-name">BIRCHMERE</span>
    </div>
  </div>
</section>

<section class="page lifecycle">
  <svg class="growth-chart" width="380" height="520" viewBox="0 0 380 520" aria-hidden="true">
    <path d="M22 338 C 150 345, 250 250, 300 135" fill="none" stroke="var(--arrow-sand)" stroke-width="9" stroke-linecap="round"/>
    <polygon points="284,140 318,108 320,158" fill="var(--arrow-sand)"/>
    <g>
      <polygon points="0,425 30,425 52,413 22,413" fill="var(--teal-top)"/>
      <rect x="0" y="425" width="30" height="95" fill="var(--teal-dark)"/>
      <rect x="30" y="425" width="22" height="95" fill="var(--teal-side)"/>
      <polygon points="68,395 98,395 120,383 90,383" fill="var(--teal-top)"/>
      <rect x="68" y="395" width="30" height="125" fill="var(--teal-dark)"/>
      <rect x="98" y="395" width="22" height="125" fill="var(--teal-side)"/>
      <polygon points="136,360 166,360 188,348 158,348" fill="var(--teal-top)"/>
      <rect x="136" y="360" width="30" height="160" fill="var(--teal-dark)"/>
      <rect x="166" y="360" width="22" height="160" fill="var(--teal-side)"/>
      <polygon points="204,320 234,320 256,308 226,308" fill="var(--teal-top)"/>
      <rect x="204" y="320" width="30" height="200" fill="var(--teal-dark)"/>
      <rect x="234" y="320" width="22" height="200" fill="var(--teal-side)"/>
      <polygon points="272,280 302,280 324,268 294,268" fill="var(--teal-top)"/>
      <rect x="272" y="280" width="30" height="240" fill="var(--teal-dark)"/>
      <rect x="302" y="280" width="22" height="240" fill="var(--teal-side)"/>
    </g>
  </svg>
  <div class="lifecycle-text">
    <h2>INVESTMENT<br>LIFECYCLE</h2>
    <ul class="steps">
      <li><svg width="12" height="10" viewBox="0 0 12 10"><path d="M1 5 L4.5 8.5 L11 1" fill="none" stroke="var(--ink)" stroke-width="1.2"/></svg>Investor frmation</li>
      <li><svg width="12" height="10" viewBox="0 0 12 10"><path d="M1 5 L4.5 8.5 L11 1" fill="none" stroke="var(--ink)" stroke-width="1.2"/></svg>Acquire asset</li>
      <li><svg width="12" height="10" viewBox="0 0 12 10"><path d="M1 5 L4.5 8.5 L11 1" fill="none" stroke="var(--ink)" stroke-width="1.2"/></svg>Reposition</li>
      <li><svg width="12" height="10" viewBox="0 0 12 10"><path d="M1 5 L4.5 8.5 L11 1" fill="none" stroke="var(--ink)" stroke-width="1.2"/></svg>Increase rents</li>
      <li><svg width="12" height="10" viewBox="0 0 12 10"><path d="M1 5 L4.5 8.5 L11 1" fill="none" stroke="var(--ink)" stroke-width="1.2"/></svg>Distribute cash flow</li>
      <li><svg width="12" height="10" viewBox="0 0 12 10"><path d="M1 5 L4.5 8.5 L11 1" fill="none" stroke="var(--ink)" stroke-width="1.2"/></svg>Asset appreciation</li>
      <li><svg width="12" height="10" viewBox="0 0 12 10"><path d="M1 5 L4.5 8.5 L11 1" fill="none" stroke="var(--ink)" stroke-width="1.2"/></svg>Re-finance or sell asset</li>
      <li><svg width="12" height="10" viewBox="0 0 12 10"><path d="M1 5 L4.5 8.5 L11 1" fill="none" stroke="var(--ink)" stroke-width="1.2"/></svg>Distribute profits</li>
    </ul>
  </div>
</section>

</body>
</html>
```